Kestrel Summit 2019 Enemies of the End-Times Church Flyer

We want a church conference flyer designed. We are looking for a professional, yet catchy design that uses our brand colors and logo creatively while communicating key information of the event effectively. <br/>The flyer must include all of the following:<br/>Title: Kestrel Summit 2019<br/>Topic: The Enemies of The End-Times Church <br/>Subtitles: <br/> -How the antichrist raises an army by social behavior engineering. <br/>-How the architects of modern social constructs escaped the church's radar. <br/>-The Holy Spirit's end-times agenda:<br/> The Knock-Out Punch!<br/>Speaker: Prophet Marcus Toliver <br/>Dates/time: December 27, 28 & 29 at 6pm<br/>Location: Halvorn Community Center <br/> 241 Pellham Street <br/> Portland, ME 04102<br/>Contact info: phone: 207-555-0148 <br/>email: contact@brookmeadow.example <br/> www.vutel.example<br/>*The flyer must also include a picture of the speaker and our Vutel logo <br/>Thanks, we look forward to seeing what you come up with!

Colors

Designer to choose colors to be used in the design.

Requirements
Must have
• The flyer must include all of the following:
• Title: Kestrel Summit 2019
• Topic: The Enemies of The End-Times Church
• Subtitles:
• -How the antichrist raises an army by social behavior engineering.
• -How the architects of modern social constructs escaped the church's radar.
• -The Holy Spirit's end-times agenda:
• The Knock-Out Punch!
• Speaker: Prophet Marcus Toliver
• Dates/time: December 27, 28 & 29 at 6pm
• Location: Halvorn Community Center
• 241 Pellham Street
• Portland, ME 04102
• Contact info: phone: 207-555-0148
• email: contact@brookmeadow.example
• www.vutel.example
• *The flyer must also include a picture of the speaker and our Vutel logo
Should not have
• Pictures of crosses or church buildings

```html
<!DOCTYPE html>
<html lang="en">
<head>
<meta charset="utf-8">
<title>Kestrel Summit 2019 – Flyer</title>
<link rel="stylesheet" href="https://fonts.googleapis.com/css2?family=Bebas+Neue&family=Roboto:wght@400;500&display=swap">
<style>
  :root {
    --navy: #003a5d;
    --red: #a2282e;
    --paper: #ecebec;
    --ink: #3d3c3d;
    --white: #ffffff;
    --accent: #f39a26;
    --display: "Bebas Neue", "Oswald", sans-serif;
    --body: "Roboto", "Helvetica Neue", Arial, sans-serif;
  }
  * { margin: 0; padding: 0; box-sizing: border-box; }
  html, body { width: 848px; height: 1200px; overflow: hidden; background: var(--paper); }
  .flyer { position: relative; width: 848px; height: 1200px; overflow: hidden; background: var(--paper); }
  .backdrop { position: absolute; inset: 0; width: 848px; height: 1200px; }

  .brand { position: absolute; left: 37px; top: 62px; height: 56px; display: flex; align-items: center; gap: 12px; }
  .brand-dot { width: 22px; height: 22px; border-radius: 50%; background: var(--accent); flex: none; }
  .brand-name { font-family: var(--display); font-weight: 400; font-size: 60px; line-height: 1; letter-spacing: 2px; color: var(--white); white-space: nowrap; }

  .event-title { position: absolute; right: 37px; top: 0; text-align: right; font-family: var(--display); color: var(--ink); font-weight: 400; }
  .event-title span { position: absolute; right: 0; display: block; line-height: 1; white-space: nowrap; }
  .title-name { top: 74px; font-size: 110px; }
  .title-kind { top: 176px; font-size: 57px; }
  .title-year { top: 230px; font-size: 106px; }

  .topic { position: absolute; left: 37px; top: 282px; font-family: var(--display); font-weight: 400; color: var(--white); font-size: 26px; line-height: 31px; }

  .agenda { position: absolute; left: 37px; top: 378px; list-style: none; font-family: var(--body); font-weight: 400; color: var(--white); font-size: 14px; line-height: 23px; text-transform: uppercase; width: 400px; }
  .agenda li { position: absolute; left: 0; padding-left: 14px; width: 400px; }
  .agenda li::before { content: "-"; position: absolute; left: 0; top: 0; }
  .agenda li:nth-child(1) { top: 0; }
  .agenda li:nth-child(2) { top: 68px; }
  .agenda li:nth-child(3) { top: 136px; }
  .agenda li:nth-child(4) { top: 181px; }

  .schedule { position: absolute; left: 37px; top: 608px; color: var(--white); font-family: var(--display); }
  .schedule-month { display: block; font-size: 58px; line-height: 1; }
  .schedule-days { position: absolute; left: 0; top: 57px; width: 112px; height: 24px; background: var(--paper); color: var(--ink); font-size: 25px; line-height: 26px; text-align: center; white-space: nowrap; }
  .schedule-time { position: absolute; left: 125px; top: 53px; font-size: 33px; line-height: 1; white-space: nowrap; }

  .speaker { position: absolute; left: 37px; top: 731px; font-family: var(--display); color: var(--white); font-size: 24px; line-height: 1; white-space: nowrap; word-spacing: 2px; }

  .contact { position: absolute; font-family: var(--body); color: var(--ink); font-weight: 400; }
  .contact-icon { position: absolute; width: 32px; height: 32px; }
  .address { left: 36px; top: 990px; }
  .address .contact-icon { left: 0; top: 18px; }
  .address p { position: absolute; left: 53px; top: 0; font-size: 15px; line-height: 24px; white-space: nowrap; }
  .phone { left: 408px; top: 1008px; }
  .phone .contact-icon { left: 0; top: 0; }
  .phone p { position: absolute; left: 44px; top: 3px; font-size: 19px; line-height: 26px; white-space: nowrap; }
  .email { left: 36px; top: 1090px; }
  .email .contact-icon { left: 0; top: 0; }
  .email p { position: absolute; left: 49px; top: 6px; font-size: 15px; line-height: 20px; white-space: nowrap; }
  .web { left: 408px; top: 1090px; }
  .web .contact-icon { left: 0; top: 0; }
  .web p { position: absolute; left: 44px; top: 6px; font-size: 15px; line-height: 20px; white-space: nowrap; }

  .footer-rule { position: absolute; left: 36px; top: 1158px; width: 776px; height: 1px; background: var(--ink); }
</style>
</head>
<body>
<main class="flyer">
  <svg class="backdrop" viewBox="0 0 1623 2296" preserveAspectRatio="none" aria-hidden="true">
    <defs>
      <linearGradient id="speaker-tone" x1="0" y1="0" x2="0" y2="1">
        <stop offset="0" stop-color="#5a3f35"/>
        <stop offset="0.3" stop-color="#7a2a2e"/>
        <stop offset="0.55" stop-color="#3a3a40"/>
        <stop offset="1" stop-color="#2b2b30"/>
      </linearGradient>
      <filter id="soft-shadow" x="-10%" y="-10%" width="120%" height="120%">
        <feDropShadow dx="-6" dy="6" stdDeviation="10" flood-color="#000" flood-opacity="0.35"/>
      </filter>
    </defs>
    <rect width="1623" height="2296" fill="var(--paper)"/>
    <polygon class="band-red" points="0,430 300,350 1623,790 1623,1895 0,1470" fill="var(--red)"/>
    <polygon class="band-navy-top" points="0,0 1612,0 0,430" fill="var(--navy)" filter="url(#soft-shadow)"/>
    <polygon class="band-navy-bottom" points="0,1470 1623,1895 1623,1935 0,1690" fill="var(--navy)"/>
  </svg>

  <svg class="backdrop" viewBox="0 0 1623 2296" preserveAspectRatio="none">
    <path class="speaker-photo" role="img" aria-label="Photo of the speaker, Prophet Marcus Toliver, seated in a dark blazer over a red sweater"
      d="M640,1880 L690,1150 Q740,990 880,935 L875,620 Q900,470 1020,460 Q1150,465 1185,600 L1200,890 Q1480,960 1535,1120 L1565,1880 Z"
      fill="url(#speaker-tone)" filter="url(#soft-shadow)"/>
  </svg>

  <div class="brand">
    <span class="brand-dot"></span>
    <span class="brand-name">VUTEL</span>
  </div>

  <h1 class="event-title">
    <span class="title-name">KESTREL</span>
    <span class="title-kind">SUMMIT</span>
    <span class="title-year">2019</span>
  </h1>

  <h2 class="topic">TOPIC :<br>THE ENEMIES OF THE END-TIMES CHURCH</h2>

  <ul class="agenda">
    <li>How the antichrist raises an army by social behavior engineering.</li>
    <li>How the architects of modern social constructs escaped the church's radar.</li>
    <li>The Holy Spirit's end-times agenda:</li>
    <li>The knock-out punch!</li>
  </ul>

  <div class="schedule">
    <span class="schedule-month">DECEMBER</span>
    <span class="schedule-days">27, 28 &amp; 29</span>
    <span class="schedule-time">AT 6PM</span>
  </div>

  <p class="speaker">SPEAKER :&nbsp; PROPHET MARCUS TOLIVER</p>

  <div class="contact address">
    <svg class="contact-icon" viewBox="0 0 32 32" aria-hidden="true">
      <circle cx="16" cy="16" r="16" fill="var(--navy)"/>
      <path d="M16 7a6 6 0 0 0-6 6c0 4.5 6 12 6 12s6-7.5 6-12a6 6 0 0 0-6-6zm0 8.3a2.3 2.3 0 1 1 0-4.6 2.3 2.3 0 0 1 0 4.6z" fill="var(--white)"/>
    </svg>
    <p>Halvorn Community Center<br>241 Pellham Street<br>Portland, ME 04102</p>
  </div>

  <div class="contact phone">
    <svg class="contact-icon" viewBox="0 0 32 32" aria-hidden="true">
      <circle cx="16" cy="16" r="16" fill="var(--navy)"/>
      <path d="M11.2 8.5l2.6-.5 1.6 4.1-1.8 1.3a9 9 0 0 0 4.9 4.9l1.3-1.8 4.1 1.6-.5 2.6c-.2.8-1 1.3-1.8 1.2C15.5 21.3 10.7 16.5 10 10.3c-.1-.8.4-1.6 1.2-1.8z" fill="var(--white)"/>
    </svg>
    <p>207-555-0148</p>
  </div>

  <div class="contact email">
    <svg class="contact-icon" viewBox="0 0 32 32" aria-hidden="true">
      <circle cx="16" cy="16" r="16" fill="var(--navy)"/>
      <rect x="8" y="10.5" width="16" height="11" rx="1" fill="none" stroke="var(--white)" stroke-width="1.6"/>
      <path d="M8.5 11l7.5 6 7.5-6M8.5 21l5.5-5M23.5 21l-5.5-5" fill="none" stroke="var(--white)" stroke-width="1.6"/>
    </svg>
    <p>contact@brookmeadow.example</p>
  </div>

  <div class="contact web">
    <svg class="contact-icon" viewBox="0 0 32 32" aria-hidden="true">
      <circle cx="16" cy="16" r="16" fill="var(--navy)"/>
      <g fill="none" stroke="var(--white)" stroke-width="1.5">
        <circle cx="16" cy="16" r="8"/>
        <ellipse cx="16" cy="16" rx="3.5" ry="8"/>
        <path d="M8 16h16M9.2 12h13.6M9.2 20h13.6"/>
      </g>
    </svg>
    <p>www.vutel.example</p>
  </div>

  <div class="footer-rule"></div>
</main>
</body>
</html>
```